Stationery Design Project

Our company is "Meridian Softworks" and we have a product called "ledgerpine.com". The product is an online accounting software for businesses. We want to communicate that our software will help business owners to be more efficient and help them track their finances better. Ledgerpine.com is basically a simple version of tallyworks.

"We want a unique and creative design which will surprise our customer."

NAME CARD = LEDGERPINE
We want a ledgerpine name card NOT MERIDIAN SOFTWORKS.

For the content of the name card, please make sure it fit with a long name like the following:

Dimas Prasetyo Alias Dimas
Developer Specialist
T: (021) 5172 4480
F: (021) 5172 4481
E: customer.service@mrd-soft.example

I need you to put it the following information to the name card

"ledgerpine"
- moto is "automate your businesses"
- website "www.ledgerpine.example"
- ledgerpine is a "Web Accounting Software"
- product of "Meridian Softworks"

LETTERHEAD, ENVELOPE, FOLDER = MERIDIAN SOFTWORKS
Other than name card we wanted you to design for us; letterhead, envelope and folder. In letterhead, envelope and folder it should ONLY contain the following information ("Meridian Softworks").
PLEASE BE SURE YOU ARE NOT PUTTING "LEDGERPINE LOGO" IN LETTERHEAD, ENVELOPE AND FOLDER.

"Meridian Softworks"
Address:
Ruko Kirana Plaza Blok. D No. 17
Jl. Wijayakusuma No. 48
Jakarta
Kebayoran, 12450
Indonesia

Web Address: mrd-soft.example

T: (021) 5172 4480
F: (021) 5172 4481

Target Market(s)

Business Owners, Accountant, Auditor, Tax Consultant

Industry/Entity Type

Accounting

```html
<!DOCTYPE html>
<html lang="en">
<head>
<meta charset="utf-8">
<title>Meridian Softworks – Stationery</title>
<link rel="stylesheet" href="https://fonts.googleapis.com/css2?family=Open+Sans:wght@400;600;700&display=swap">
<style>
:root{
  --bg:#eceded;
  --paper:#ffffff;
  --ink:#6b6e72;
  --ink-dark:#44474b;
  --green:#7ea844;
  --blue:#4a86c2;
  --folder-top:#a3a6aa;
  --folder-bottom:#717478;
  --strip:#5d6064;
  --shadow:0 2px 6px rgba(0,0,0,.12);
}
*{box-sizing:border-box;margin:0;padding:0}
html,body{width:1200px;height:794px;overflow:hidden}
body{background:var(--bg);font-family:"Open Sans",Arial,sans-serif;color:var(--ink);position:relative}
.sheet{position:absolute;background:var(--paper);box-shadow:var(--shadow)}

.brand{display:flex;align-items:center;gap:8px;white-space:nowrap}
.brand-dot{width:22px;height:22px;border-radius:50%;background:var(--green);flex:none}
.brand-name{font-weight:600;color:var(--ink);letter-spacing:.12em;font-size:15px;line-height:1.1;text-transform:uppercase}

.contact-row{position:absolute;display:flex;font-size:6.5px;line-height:1.5;color:var(--ink);white-space:nowrap}
.contact-col{display:flex;gap:5px;padding:0 9px;border-left:1px solid var(--blue)}
.contact-col:first-child{border-left:none;padding-left:0}
.contact-col svg{width:8px;height:8px;flex:none;margin-top:1px;fill:var(--ink)}

/* business cards */
.card{width:260px;height:150px}
.card-front{left:70px;top:40px;padding:24px 22px}
.card-front .person{font-size:13px;font-weight:600;color:var(--ink-dark);white-space:nowrap}
.card-front .role{font-size:8px;color:var(--green);margin-bottom:22px}
.card-front .lines{font-size:8px;line-height:1.6;white-space:nowrap}
.card-back{left:70px;top:210px;padding:22px}
.card-back .product{display:flex;align-items:center;gap:10px}
.product-name{background:var(--ink-dark);color:#fff;font-size:12px;font-weight:600;padding:5px 9px}
.product-note{border-left:1px solid var(--blue);padding-left:8px;font-size:7px;line-height:1.5;white-space:nowrap}
.card-back .motto{margin-top:30px;display:flex;align-items:center;gap:10px}
.card-back .motto .brand-name{font-size:10px}
.card-back .motto .brand-dot{width:14px;height:14px}
.tagline{border-left:1px solid var(--blue);padding-left:8px;font-size:8px;white-space:nowrap}
.card-back .web{position:absolute;right:22px;bottom:14px;font-size:7px}

/* letterhead */
.letterhead{left:360px;top:30px;width:360px;height:509px}
.letterhead .brand{position:absolute;left:30px;top:28px}
.letterhead .contact-row{left:30px;bottom:40px}

/* folder */
.folder{left:750px;top:30px;width:380px;height:509px;overflow:hidden;
  background:linear-gradient(160deg,var(--folder-top),var(--folder-bottom))}
.folder-strip{position:absolute;left:0;top:0;right:0;height:22px;background:var(--strip)}
.folder-band{position:absolute;left:0;right:0;top:22px;height:88px;background:var(--paper);
  display:flex;align-items:center;padding:0 22px;gap:12px}
.folder-band .brand-name{font-size:15px}
.folder-band .brand-dot{width:26px;height:26px}
.folder-band .tagline{font-size:12px;padding-left:10px;line-height:28px}

/* envelope */
.envelope{left:165px;top:570px;width:420px;height:194px}
.envelope .brand{position:absolute;left:24px;top:20px}
.envelope .contact-row{left:24px;top:130px}

/* compliments slip */
.compliments{left:615px;top:570px;width:420px;height:194px}
.compliments .brand{position:absolute;left:24px;top:20px}
.compliments .slip-title{position:absolute;right:26px;top:96px;font-size:16px;font-weight:700;color:var(--ink)}
.compliments .contact-row{left:24px;top:140px}
</style>
</head>
<body>
<svg width="0" height="0" style="position:absolute" aria-hidden="true">
  <symbol id="icon-pin" viewBox="0 0 10 10"><path d="M5 0a3.5 3.5 0 0 0-3.5 3.5C1.5 6 5 10 5 10s3.5-4 3.5-6.5A3.5 3.5 0 0 0 5 0zm0 5a1.4 1.4 0 1 1 0-2.8A1.4 1.4 0 0 1 5 5z"/></symbol>
  <symbol id="icon-phone" viewBox="0 0 10 10"><path d="M2 0l2 2.5-1 1.2a6 6 0 0 0 3.3 3.3l1.2-1L10 8l-1 2C4 10 0 6 0 1z"/></symbol>
  <symbol id="icon-mail" viewBox="0 0 10 10"><path d="M0 2h10v6H0zm1 1v.3l4 2.5 4-2.5V3z"/></symbol>
</svg>

<!-- name card: front -->
<section class="sheet card card-front">
  <p class="person">Dimas Prasetyo Alias Dimas</p>
  <p class="role">Developer Specialist</p>
  <div class="lines">
    <p>T: (021) 5172 4480</p>
    <p>F: (021) 5172 4481</p>
    <p>E: customer.service@mrd-soft.example</p>
  </div>
</section>

<!-- name card: back -->
<section class="sheet card card-back">
  <div class="product">
    <span class="product-name">ledgerpine</span>
    <p class="product-note">Web Accounting Software<br>product of Meridian Softworks</p>
  </div>
  <div class="motto">
    <span class="brand"><span class="brand-dot"></span><span class="brand-name">ledgerpine</span></span>
    <span class="tagline">automate your businesses</span>
  </div>
  <p class="web">www.ledgerpine.example</p>
</section>

<!-- letterhead -->
<section class="sheet letterhead">
  <div class="brand"><span class="brand-dot"></span><span class="brand-name">Meridian Softworks</span></div>
  <div class="contact-row">
    <div class="contact-col"><svg><use href="#icon-pin"/></svg><p>Ruko Kirana Plaza Blok. D No. 17<br>Jl. Wijayakusuma No. 48<br>Jakarta, Kebayoran, 12450<br>Indonesia</p></div>
    <div class="contact-col"><svg><use href="#icon-phone"/></svg><p>T: (021) 5172 4480<br>F: (021) 5172 4481</p></div>
    <div class="contact-col"><svg><use href="#icon-mail"/></svg><p>info@mrd-soft.example<br>mrd-soft.example</p></div>
  </div>
</section>

<!-- folder -->
<section class="sheet folder">
  <div class="folder-strip"></div>
  <div class="folder-band">
    <div class="brand"><span class="brand-dot"></span><span class="brand-name">Meridian Softworks</span></div>
    <span class="tagline">Count Smarter</span>
  </div>
</section>

<!-- envelope -->
<section class="sheet envelope">
  <div class="brand"><span class="brand-dot"></span><span class="brand-name">Meridian Softworks</span></div>
  <div class="contact-row">
    <div class="contact-col"><svg><use href="#icon-pin"/></svg><p>Ruko Kirana Plaza Blok. D No. 17<br>Jl. Wijayakusuma No. 48<br>Jakarta, Kebayoran, 12450, Indonesia</p></div>
    <div class="contact-col"><svg><use href="#icon-phone"/></svg><p>T: (021) 5172 4480<br>F: (021) 5172 4481</p></div>
    <div class="contact-col"><svg><use href="#icon-mail"/></svg><p>info@mrd-soft.example<br>mrd-soft.example</p></div>
  </div>
</section>

<!-- compliments slip -->
<section class="sheet compliments">
  <div class="brand"><span class="brand-dot"></span><span class="brand-name">Meridian Softworks</span></div>
  <p class="slip-title">With Compliments</p>
  <div class="contact-row">
    <div class="contact-col"><svg><use href="#icon-pin"/></svg><p>Ruko Kirana Plaza Blok. D No. 17<br>Jl. Wijayakusuma No. 48<br>Jakarta, Kebayoran, 12450, Indonesia</p></div>
    <div class="contact-col"><svg><use href="#icon-phone"/></svg><p>T: (021) 5172 4480<br>F: (021) 5172 4481</p></div>
    <div class="contact-col"><svg><use href="#icon-mail"/></svg><p>info@mrd-soft.example<br>mrd-soft.example</p></div>
  </div>
</section>
</body>
</html>
```